Real estate investment and development Business Visiting cards

Visiting cards for our company
We develop flats and rent them out, Now we planning to offer investors new investment opportunities in the UK Real estate sector. we used to have a design for our visiting card but we do not like it anymore. we want to have different designs keeping the same colors with our websites and company. I will attach our previous Visiting card model.

Target Market(s)

Private Investors, Banks,

Industry/Entity Type

Real Estate Development

Contact Information for Business Card

TRVK Holdings
Deren Moston Director
Info to be included
3-Info

Tel
(+44 )7481 392715

Email

deren@trvk.co.uk

info@trvk.co.uk

Address

47 Harlow Finch Road, Brenmore, Calderwick, CW4 3QT

Website

trvkholdings.co.uk

Font styles to use
Serif

Colors
f78f20
fef5ee

Requirements
Must have
• The colours of the company and the Logo
Nice to have
• Modern idea and icons on the info
A code bar that directs to the website
Should not have
• a lot from the orange colour

```html
<!DOCTYPE html>
<html lang="en">
<head>
<meta charset="utf-8">
<title>TRVK Holdings – Business Card</title>
<link href="https://fonts.googleapis.com/css2?family=Libre+Baskerville:wght@400&family=Roboto:wght@400;700&display=swap" rel="stylesheet">
<style>
  :root {
    --orange: #f78f20;
    --cream: #fef5ee;
    --ink: #2b2b2b;
    --muted: #555555;
    --card-black: #1c1c1e;
    --pattern-light: #3a3a3d;
    --pattern-dark: #19191b;
    --stage: #3b3b3d;
    --paper: #ffffff;
  }
  * { margin: 0; padding: 0; box-sizing: border-box; }
  html, body { width: 799px; height: 1200px; overflow: hidden; }
  body {
    background: var(--stage);
    font-family: "Roboto", Arial, sans-serif;
    position: relative;
  }
  .card {
    position: absolute;
    left: 89px;
    width: 620px;
    height: 354px;
    overflow: hidden;
    box-shadow: 0 8px 24px rgba(0,0,0,0.35);
  }
  .card--front { top: 123px; background: var(--card-black); }
  .card--back { top: 723px; background: var(--paper); }

  /* Front */
  .front-pattern {
    position: absolute; inset: 0;
    background: linear-gradient(135deg, var(--pattern-dark) 0%, var(--pattern-light) 55%, var(--pattern-dark) 100%);
  }
  .front-brand {
    position: absolute;
    right: 60px;
    bottom: 96px;
    display: flex;
    align-items: center;
    gap: 14px;
  }
  .brand-square {
    width: 46px; height: 46px;
    background: var(--orange);
  }
  .front-brand__name {
    font-family: "Libre Baskerville", Georgia, serif;
    font-size: 40px;
    letter-spacing: 1px;
    color: var(--paper);
    line-height: 1;
  }

  /* Back */
  .back-tab {
    position: absolute;
    left: -22px; top: 6px;
    width: 40px; height: 40px;
    border-radius: 50%;
    background: var(--orange);
  }
  .holder {
    position: absolute; left: 34px; top: 22px;
  }
  .holder__name {
    font-weight: 700; font-size: 17px; letter-spacing: 0.5px;
    color: var(--orange); text-transform: uppercase;
  }
  .holder__role { font-size: 11px; color: var(--muted); margin-top: 2px; }

  .contact {
    position: absolute; left: 34px; top: 112px;
    font-size: 13px; color: var(--ink); line-height: 1.35;
  }
  .contact__company { font-weight: 700; color: var(--orange); font-size: 13px; }
  .contact__address { margin-bottom: 10px; }
  .contact__row { display: flex; align-items: center; gap: 9px; }
  .contact__icon { width: 12px; height: 12px; flex: none; }
  .web-accent { color: var(--orange); }

  .back-brand {
    position: absolute;
    right: 50px; bottom: 60px;
    display: flex; align-items: center; gap: 16px;
  }
  .back-brand .brand-square { width: 70px; height: 70px; }
  .back-brand__name {
    font-family: "Roboto", Arial, sans-serif;
    font-weight: 700; font-size: 64px;
    color: var(--orange); line-height: 1;
  }
</style>
</head>
<body>

<section class="card card--front">
  <div class="front-pattern" role="img" aria-label="Embossed repeating monogram pattern in dark grey across the card"></div>
  <div class="front-brand">
    <span class="brand-square"></span>
    <span class="front-brand__name">TRVK</span>
  </div>
</section>

<section class="card card--back">
  <span class="back-tab"></span>
  <div class="holder">
    <p class="holder__name">Deren Moston</p>
    <p class="holder__role">Director</p>
  </div>

  <div class="contact">
    <p class="contact__company">TRVK Holdings</p>
    <p class="contact__address">47 Harlow Finch Road,<br>Brenmore, Calderwick, CW4 3QT</p>

    <p class="contact__row">
      <svg class="contact__icon" viewBox="0 0 24 24"><path fill="#f78f20" d="M6.6 10.8a15.2 15.2 0 0 0 6.6 6.6l2.2-2.2c.3-.3.7-.4 1-.2 1.1.4 2.3.6 3.6.6.6 0 1 .4 1 1V20c0 .6-.4 1-1 1A17 17 0 0 1 3 4c0-.6.4-1 1-1h3.5c.6 0 1 .4 1 1 0 1.3.2 2.5.6 3.6.1.3 0 .7-.2 1z"/></svg>
      <span>(+44 )7481 392715</span>
    </p>
    <p class="contact__row">
      <svg class="contact__icon" viewBox="0 0 24 24"><path fill="#f78f20" d="M2 5h20v14H2z"/><path fill="none" stroke="#fff" stroke-width="1.8" d="M2.5 5.5 12 13l9.5-7.5"/></svg>
      <span>deren@trvk.co.uk</span>
    </p>
    <p class="contact__row">
      <svg class="contact__icon" viewBox="0 0 24 24"><path fill="#f78f20" d="M2 5h20v14H2z"/><path fill="none" stroke="#fff" stroke-width="1.8" d="M2.5 5.5 12 13l9.5-7.5"/></svg>
      <span>info@trvk.co.uk</span>
    </p>
    <p class="contact__row">
      <svg class="contact__icon" viewBox="0 0 24 24"><circle cx="12" cy="12" r="10" fill="#f78f20"/><path fill="none" stroke="#fff" stroke-width="1.5" d="M2 12h20M12 2c3 3 3 17 0 20M12 2c-3 3-3 17 0 20"/></svg>
      <span>www.<span class="web-accent">trvkholdings</span>.co.uk</span>
    </p>
  </div>

  <div class="back-brand">
    <span class="brand-square"></span>
    <span class="back-brand__name">TRVK</span>
  </div>
</section>

</body>
</html>
```